Roofing Company Now Hiring and Call Now Facebook Ads

Trying to hire new sales reps in our Alabama market to add to our growing team. This is a great opportunity for any one looking for a career change or looking to add time back to the time they get to spend at home with their families. This is a chance to build a career in one of the fastest growing industries in the country and build financial freedom and a solid future for your family while easily making 6 figures yearly. Sales reps get to set their own schedule, take vacations when they want, and could even choose if they wanted to work in the summer or the winter seasons if they dont like the heat/cold environment. Sales reps are commission based with bonus/incentives for completing task and assignments weekly.

"Let's Talk About Your Roof!" Schedule a free Roof Inspection today!

Needing facebook ads for hiring and a few ads templates for daily post regarding roof inspections and roof replacements, if they are editable it would be easier for me to manage a few templates. This project needs to have a swag/cleanish look that attracts the younger group of people but still make the older group of customer think, man these guys have some solid looking things going on and looks like a well managed and built company. We also target the upper scale areas when seeking customers.

Lets see what yall got! lets Gooo!

Target Market(s)

Property owners, sales reps, homeowners, property managers, job seekers

Industry/Entity Type

Roofing Contractor Storm Restoration Contractor, Construction Contractor

Font styles to use
Sans Serif

Colors
EB3D1F
EC4F4E
F09395
F8D3D4
FCEDEE

Requirements
Must have
• Clean modern professional look with visible red and black colors, we like white too.
Nice to have
• red, black, white, popping eye catching colors.
Should not have
• wrong color red, red is more of a kelvard herons red, please stay away from the pinkish red.

```html
<!DOCTYPE html>
<html lang="en">
<head>
<meta charset="utf-8">
<title>Ridgeline Roofing – Best Roofing Services</title>
<link rel="stylesheet" href="https://fonts.googleapis.com/css2?family=Montserrat:wght@600;700;800&family=Roboto:wght@300;400&display=swap">
<style>
  :root {
    --red: #eb3d1f;
    --red-soft: #ec4f4e;
    --charcoal: #3b3b3d;
    --white: #ffffff;
    --mist: #e6e6e8;
    --square-grey: #a9a9ab;
    --font-display: "Montserrat", Arial, sans-serif;
    --font-body: "Roboto", Arial, sans-serif;
  }
  * { margin: 0; padding: 0; box-sizing: border-box; }
  html, body { width: 1200px; height: 1200px; overflow: hidden; background: var(--white); }
  .ad {
    position: relative;
    width: 1080px;
    height: 1080px;
    transform: scale(1.11111);
    transform-origin: 0 0;
    overflow: hidden;
    background: var(--white);
  }
  .ad__shapes { position: absolute; inset: 0; }
  .brand {
    position: absolute;
    left: 80px;
    top: 64px;
    font-family: var(--font-display);
    font-weight: 700;
    font-size: 26px;
    line-height: 1;
    color: var(--red);
  }
  .headline {
    position: absolute;
    left: 80px;
    top: 252px;
    font-family: var(--font-display);
    font-weight: 800;
    font-size: 70px;
    line-height: 78px;
    color: var(--white);
    letter-spacing: 0.5px;
  }
  .headline__dark { color: var(--charcoal); }
  .rule {
    position: absolute;
    left: 85px;
    top: 506px;
    width: 128px;
    height: 3px;
    background: var(--white);
  }
  .intro {
    position: absolute;
    left: 80px;
    top: 538px;
    width: 570px;
    font-family: var(--font-body);
    font-weight: 300;
    font-size: 27px;
    line-height: 38px;
    color: var(--white);
  }
  .services-title {
    position: absolute;
    left: 80px;
    top: 830px;
    font-family: var(--font-display);
    font-weight: 800;
    font-size: 33px;
    color: var(--white);
  }
  .services-title span { color: var(--charcoal); }
  .services {
    position: absolute;
    left: 79px;
    top: 906px;
    list-style: none;
    font-family: var(--font-display);
    font-weight: 600;
    font-size: 18.5px;
    color: var(--white);
  }
  .services li { position: absolute; white-space: nowrap; display: flex; align-items: center; gap: 22px; }
  .services li::before { content: ""; width: 22px; height: 22px; background: var(--white); }
  .contact-title {
    position: absolute;
    left: 770px;
    top: 853px;
    font-family: var(--font-display);
    font-weight: 800;
    font-size: 34px;
    color: var(--charcoal);
  }
  .contact {
    position: absolute;
    left: 775px;
    top: 920px;
    list-style: none;
    font-family: var(--font-body);
    font-weight: 400;
    font-size: 21px;
    line-height: 35px;
    color: var(--charcoal);
  }
  .contact li { display: flex; align-items: center; gap: 20px; }
  .contact li::before { content: ""; width: 13px; height: 13px; background: var(--square-grey); }
</style>
</head>
<body>
<div class="ad">
  <svg class="ad__shapes" width="1080" height="1080" viewBox="0 0 1080 1080" aria-hidden="false">
    <defs>
      <linearGradient id="redFill" x1="0" y1="0" x2="0" y2="1">
        <stop offset="0" stop-color="#eb3d1f"/>
        <stop offset="1" stop-color="#ec4f4e"/>
      </linearGradient>
      <linearGradient id="photoTone" x1="0" y1="0" x2="1" y2="1">
        <stop offset="0" stop-color="#8a9a78"/>
        <stop offset="0.45" stop-color="#c9a7a3"/>
        <stop offset="0.75" stop-color="#e7e3dc"/>
        <stop offset="1" stop-color="#d4c6b3"/>
      </linearGradient>
    </defs>
    <circle class="photo-area" cx="850" cy="200" r="450" fill="url(#photoTone)" role="img" aria-label="Photo of a roofer in a hard hat on a ladder fitting a gutter under a red tile roof"/>
    <circle class="accent-circle" cx="150" cy="720" r="565" fill="url(#redFill)"/>
    <circle class="contact-circle" cx="900" cy="1010" r="265" fill="#e6e6e8"/>
  </svg>

  <div class="brand">Ridgeline Roofing</div>

  <h1 class="headline">BEST<br>ROOFING<br><span class="headline__dark">SERVICES</span></h1>
  <div class="rule"></div>

  <p class="intro">Ridgeline is a family-owned business that has been around for many years, and it shows in the work we do. We believe in honesty with our clients. Transparency and respect are part of our core values that make Ridgeline a customer-centric company.</p>

  <h2 class="services-title">OUR <span>SEVICES:</span></h2>
  <ul class="services">
    <li style="left:0;top:0">RESIDENTIAL ROOFING</li>
    <li style="left:0;top:43px">COMMERCIAL ROOFING</li>
    <li style="left:0;top:86px">GUTTERS</li>
    <li style="left:188px;top:86px">SIDING</li>
  </ul>

  <h2 class="contact-title">CONTACT:</h2>
  <ul class="contact">
    <li>(555) 014-2290</li>
    <li>info@ridgelinerf.com</li>
    <li>Dalewood, GA</li>
  </ul>
</div>
</body>
</html>
```